TARO PTY LTD - Business Cards

Design a modern business card - using the attached Designs.
Same design as on the front, apart from the names/numbers/emails to be different.
We want the cards to be very glossy to stand out, do I think the simple black/white/metallic will be effective.
Both lots of details below:

Lyle Marrick
Director
lyle_taro@quintmail.example
0493 628 304

Simon Prowle
Director
simon_taro@quintmail.example
0438 514 209

```html
<!DOCTYPE html>
<html lang="en">
<head>
<meta charset="utf-8">
<title>TARO PTY LTD – Business Cards</title>
<link rel="stylesheet" href="https://fonts.googleapis.com/css2?family=Open+Sans:wght@400;600&display=swap">
<style>
  :root {
    --page: #ffffff;
    --carbon-dark: #0d0d0d;
    --carbon-mid: #1f1f1f;
    --steel-light: #d9d9d9;
    --steel-mid: #9a9a9a;
    --steel-dark: #4a4a4a;
    --band: rgba(28, 28, 28, 0.92);
    --text-main: #f2f2f2;
    --text-soft: #8c8c8c;
    --text-phone: #a8a8a8;
    --brand: #d4d4d4;
  }
  html, body {
    margin: 0;
    width: 1200px;
    height: 1000px;
    overflow: hidden;
    background: var(--page);
    font-family: "Open Sans", Arial, sans-serif;
  }
  .canvas { position: relative; width: 1200px; height: 1000px; }
  .card {
    position: absolute;
    left: 366px;
    width: 409px;
    height: 238px;
    overflow: hidden;
    box-shadow: 4px 5px 5px rgba(0, 0, 0, 0.55);
  }
  .card--front { top: 69px; }
  .card--lyle { top: 373px; }
  .card--simon { top: 678px; }

  .carbon {
    position: absolute; inset: 0;
    background: linear-gradient(160deg, var(--carbon-mid) 0%, var(--carbon-dark) 55%, #050505 100%);
  }
  .steel {
    position: absolute;
    background: linear-gradient(180deg, var(--steel-dark) 0%, var(--steel-light) 22%, var(--steel-mid) 45%, var(--steel-dark) 60%, var(--steel-mid) 78%, var(--steel-light) 90%, var(--steel-dark) 100%);
  }
  .card--front .steel {
    left: 97px; width: 207px; top: 0; bottom: 0;
    background: radial-gradient(ellipse at 50% 45%, var(--steel-light) 0%, var(--steel-mid) 45%, var(--steel-dark) 100%);
  }
  .card--back .steel { inset: 0; }
  .card--back .carbon { clip-path: polygon(266px 0, 409px 0, 409px 238px, 177px 238px); }

  .band {
    position: absolute;
    left: 0; top: 82px; width: 240px; height: 82px;
    background: var(--band);
    clip-path: polygon(0 0, 240px 0, 212px 82px, 0 82px);
  }
  .contact { position: absolute; left: 46px; top: 90px; line-height: 1; }
  .contact__name { font-size: 16px; font-weight: 400; color: var(--text-main); margin: 0; }
  .contact__role { font-size: 8px; color: var(--text-soft); margin: 2px 0 0; }
  .contact__email { font-size: 9.5px; color: var(--text-soft); margin: 1px 0 0; }
  .contact__phone { font-size: 13px; font-weight: 600; color: var(--text-phone); margin: 4px 0 0; letter-spacing: 0.3px; }

  .brand {
    position: absolute;
    display: flex; align-items: center; gap: 8px;
    font-weight: 600; color: var(--brand); letter-spacing: 2px;
    transform: translate(-50%, -50%);
  }
  .brand__dot { border-radius: 50%; background: var(--brand); }
  .card--front .brand { left: 201px; top: 121px; font-size: 40px; }
  .card--front .brand__dot { width: 14px; height: 14px; }
  .card--back .brand { left: 317px; top: 124px; font-size: 30px; }
  .card--back .brand__dot { width: 10px; height: 10px; }
</style>
</head>
<body>
<main class="canvas">
  <section class="card card--front">
    <div class="carbon" role="img" aria-label="Black carbon-fibre texture"></div>
    <div class="steel" role="img" aria-label="Brushed steel plate"></div>
    <div class="brand"><span class="brand__dot"></span>TARO</div>
  </section>

  <section class="card card--back card--lyle">
    <div class="steel" role="img" aria-label="Brushed steel texture"></div>
    <div class="carbon" role="img" aria-label="Black carbon-fibre texture"></div>
    <div class="band"></div>
    <div class="contact">
      <p class="contact__name">Lyle Marrick</p>
      <p class="contact__role">Director</p>
      <p class="contact__email">lyle_taro@quintmail.example</p>
      <p class="contact__phone">0493 628 304</p>
    </div>
    <div class="brand"><span class="brand__dot"></span>TARO</div>
  </section>

  <section class="card card--back card--simon">
    <div class="steel" role="img" aria-label="Brushed steel texture"></div>
    <div class="carbon" role="img" aria-label="Black carbon-fibre texture"></div>
    <div class="band"></div>
    <div class="contact">
      <p class="contact__name">Simon Prowle</p>
      <p class="contact__role">Director</p>
      <p class="contact__email">simon_taro@quintmail.example</p>
      <p class="contact__phone">0438 514 209</p>
    </div>
    <div class="brand"><span class="brand__dot"></span>TARO</div>
  </section>
</main>
</body>
</html>
```